Book Cover Design Project

I need a book cover for a book that we will be releasing in the next few months.

It is a business book aimed at small businesses and people who want to escape the 9 - 5 and start their own business.

We want it to look similar to: http://www.tolvanbrook.example/wp-content/uploads/2010/03/fold-up.jpg and also the book designs that I have uploaded images for.

I quite like the grey / charcoal background and the bright lime green colours from the Quiet Harbor logo that I have attached. However, anything bright would be good - I am prepared to be flexible with colours. The books I have attached are a high impact as well - being bright blue with white black font with a really cool font.

The book is titled:

The Lantern Shop Plan

By Dale Vortan

Still thinking of the tagline, for now just use "Start an Online Business in no time at all"

Room for a quote/testimonial on the front of the book at the bottom, and as well on the back.

For the back cover text just use dummy text and my photo that is attached for now as well.

Barcode ISBN on the back at the bottom - price will be $19.95

Needs to be in PSD so we can change the text from our end.

I really want to get a good template made that I can edit the text for as we are still developing the book, but I want to get the book cover done so I can start advertising that it will be arriving soon.

There will probably be alterations that I need help with later down the track so looking to work with someone closely on this, and I will pay you for any extra time down the track..

Sizes will probably be around: I think 20.5cm tall and 14cm wide would be good..

Not sure how thick for the spine, it will depend on how many words get cut off, but as an estimate probably 1.5CM..
Updates

Just added some more detail to the brief.. Please read it carefully.

Target Market(s)

small business owners, professionals who want to start their own business, soon to be entrepreneurs, entrepreneurs

Industry/Entity Type

Advertising

Requirements
Must have
• The Lantern Shop Plan

and Dale Vortan must be prominent.

Tag line should be look cool under the title.

Must be very modern and cool. Needs to catch people's eyes so needs to be really punchy.

Nice to have
• Maybe a clock or stopwatch icon would be cool to add in there so it isn't just plain.. Similar to like how the books have a cool icon with them that I have attached in the uploaded images.
Should not have
• I like simplicity, artistic and very high impact. It really needs to draw you in and catch your eye.

Don't use plain boring fonts. Although I like simplicity slick design is very important - I dont want it to be boring - it has to look high quality and expensive. Therefore do not use fonts like Arial, Times New Roman those really boring fonts that make it look cheap. If I was going to do something like that then I might as well do it myself.

If you want to see the quality of things that I am usually involved with look at the artwork for one of my events that I run called Daybreaker: http://www.daybreaker.example/daybreaker-festival-anthems-ft-loomsparrow-harvest-night-eve-metro-report/

That will give you an idea of what type of quality things that I am involved with, so you need to be up for the task..

```html
<!DOCTYPE html>
<html lang="en">
<head>
<meta charset="utf-8">
<title>The Lantern Shop Plan – Cover Spread</title>
<link href="https://fonts.googleapis.com/css2?family=Bebas+Neue&family=Noto+Sans:wght@400&family=Open+Sans:wght@400&display=swap" rel="stylesheet">
<style>
  :root {
    --backdrop: #dcdcdc;
    --paper: #f2f2f2;
    --guide: #59e6ee;
    --teal: #35bfc2;
    --teal-deep: #21a3a8;
    --teal-light: #8fdcdc;
    --slate: #4f6670;
    --body-ink: #4a5560;
    --frame: #ffffff;
  }
  * { margin: 0; padding: 0; box-sizing: border-box; }
  html, body { width: 1200px; height: 1000px; overflow: hidden; }
  body { background: var(--backdrop); position: relative; font-family: "Noto Sans", sans-serif; }

  .spread { position: absolute; left: 4px; top: 80px; width: 1186px; height: 815px; background: var(--paper); overflow: hidden; }
  .guides { position: absolute; left: 0; top: 0; pointer-events: none; }

  /* back cover */
  .author-photo { position: absolute; left: 40px; top: 122px; width: 146px; height: 188px; background: var(--frame); padding: 3px; }
  .author-photo div { width: 100%; height: 100%; background: linear-gradient(160deg, #8a8a8a, #3a3a3a 55%, #1d1d1d); }
  .blurb { position: absolute; font-size: 9.8px; line-height: 24px; color: var(--body-ink); text-align: justify; hyphens: auto; }
  .blurb-intro { left: 202px; top: 175px; width: 328px; }
  .blurb-main { left: 49px; top: 321px; width: 482px; }
  .copyright { position: absolute; left: 35px; top: 758px; font-size: 10px; color: var(--body-ink); }
  .barcode-box { position: absolute; left: 314px; top: 714px; width: 128px; height: 61px; background: var(--frame); }
  .price { position: absolute; left: 460px; top: 738px; font-family: "Bebas Neue", sans-serif; font-size: 20px; line-height: 18px; color: var(--slate); }
  .price span { display: block; color: var(--teal); }

  /* spine */
  .spine-title { position: absolute; left: 566px; top: 63px; width: 62px; height: 520px; }
  .spine-title p { position: absolute; left: 0; top: 0; width: 520px; transform-origin: 0 0; transform: translate(62px, 0) rotate(90deg);
    font-family: "Bebas Neue", sans-serif; font-size: 66px; line-height: 62px; color: var(--teal); white-space: nowrap; }

  /* front cover */
  .stopwatch-mark { position: absolute; left: 646px; top: 38px; width: 340px; height: 640px;
    background: radial-gradient(ellipse 50% 42% at 50% 52%, rgba(143,220,220,0.28), rgba(143,220,220,0.08) 70%, rgba(143,220,220,0) 100%); }
  .front-title { position: absolute; left: 716px; top: 134px; width: 385px; font-family: "Bebas Neue", sans-serif; font-weight: 400;
    background: linear-gradient(90deg, var(--teal-deep), var(--teal) 70%, var(--teal-light));
    -webkit-background-clip: text; background-clip: text; color: transparent; white-space: nowrap; }
  .front-title .line-top { display: block; font-size: 64px; line-height: 70px; }
  .front-title .line-main { display: block; font-size: 126px; line-height: 106px; }
  .byline { position: absolute; right: 87px; top: 326px; font-family: "Bebas Neue", sans-serif; color: var(--teal-deep); font-size: 38px; line-height: 40px; white-space: nowrap; }
  .byline small { font-size: 24px; color: var(--teal); margin-right: 4px; }
  .tagline { position: absolute; left: 646px; width: 523px; top: 465px; text-align: center; font-family: "Open Sans", sans-serif; font-size: 20px; color: var(--slate); }
  .front-quote { position: absolute; left: 664px; width: 490px; top: 727px; text-align: center; font-size: 9.2px; line-height: 12.5px; color: #555d63; text-shadow: 0 1px 1px rgba(0,0,0,0.25); }
</style>
</head>
<body>
  <section class="spread">
    <div class="author-photo"><div role="img" aria-label="Black and white portrait photo of the author"></div></div>
    <p class="blurb blurb-intro">Global growth slowed in 2012, but some improvement in economic conditions late in the year points to a modest reacceleration of activity in 2013. While the growth outlook for a number of large economies remains subdued and the global economy vulnerable to new setbacks, risks appear more balanced at the start of 2013 based on an improved outlook in the United States and China.</p>
    <p class="blurb blurb-main">In original terms, mineral exploration expenditure fell 7.9% (or –$70.8m) to $823.9m in the December quarter 2012. The largest fall by minerals sought came from expenditure on gold exploration (down 16.3% or –$31.7m). The next largest fall came from expenditure on coal exploration (down 12.5% or –$21.4m).In original terms, mineral exploration expenditure fell 7.9% (or –$70.8m) to $823.9m in the December quarter 2012. The largest fall by minerals sought came from expenditure on gold exploration (down 16.3% or –$31.7m). The next largest fall came from expenditure on coal exploration (down 12.5% or –$21.4m).</p>
    <p class="copyright">©2013 Merrow L.P. All Rights Reserved.</p>
    <div class="barcode-box"></div>
    <p class="price">Price<span>$19.95</span></p>

    <div class="spine-title"><p>The Lantern Shop Plan</p></div>

    <div class="stopwatch-mark" role="img" aria-label="Faint watercolour stopwatch illustration"></div>
    <h1 class="front-title"><span class="line-top">The Lantern Shop</span><span class="line-main">Plan</span></h1>
    <p class="byline"><small>By</small>Dale Vortan</p>
    <p class="tagline">"Start an Online Business in no time at all"</p>
    <p class="front-quote">Strong investment in new mines and the expansion of existing operations are expected to boost production volumes in 2012-13 for key bulk commodities, though across the industry as a whole the forecast is for mixed results.</p>

    <svg class="guides" width="1186" height="815" viewBox="0 0 1186 815">
      <g stroke="var(--guide)" stroke-width="1">
        <line x1="19.5" y1="0" x2="19.5" y2="815"/>
        <line x1="544.5" y1="0" x2="544.5" y2="815"/>
        <line x1="561.5" y1="0" x2="561.5" y2="815"/>
        <line x1="628.5" y1="0" x2="628.5" y2="815"/>
        <line x1="645.5" y1="0" x2="645.5" y2="815"/>
        <line x1="1169.5" y1="0" x2="1169.5" y2="815"/>
        <line x1="0" y1="17.5" x2="1186" y2="17.5"/>
        <line x1="0" y1="786.5" x2="1186" y2="786.5"/>
      </g>
    </svg>
  </section>
</body>
</html>
```